Letterhead design for business

Looking for an attractive and professional letterhead that uses the logo that is attached below.

Target Market(s)

Potential bankruptcy clients.

Industry/Entity Type

Legal

Colors

Designer to choose colors to be used in the design.

Requirements
Must have
• Address for locations, phone number, and website address.
• Addresses are on website ferncoveadvice.example. Use following phone number (for tracking purposes): 555-013-8274

```html
<!DOCTYPE html>
<html lang="en">
<head>
<meta charset="utf-8">
<title>Ferncove Law Group Letterhead</title>
<link href="https://fonts.googleapis.com/css2?family=Dosis:wght@500&family=Arimo:wght@400;700&display=swap" rel="stylesheet">
<style>
  :root {
    --backdrop: #c9c8cd;
    --paper: #ffffff;
    --fern: #94c38b;
    --fern-dark: #6fae64;
    --charcoal: #4a4a4a;
    --ink: #333333;
    --silver: #e4e4e4;
  }
  html, body {
    margin: 0;
    padding: 0;
    width: 1200px;
    height: 878px;
    overflow: hidden;
    background: var(--backdrop);
  }
  .canvas {
    position: relative;
    width: 1200px;
    height: 878px;
  }
  .sheet {
    position: absolute;
    top: 126px;
    width: 477px;
    height: 618px;
    overflow: hidden;
  }
  .sheet--front {
    left: 105px;
    background: var(--paper);
  }
  .sheet--back {
    left: 630px;
    background: var(--fern);
  }
  .brand {
    position: absolute;
    left: 40px;
    top: 56px;
    display: flex;
    align-items: center;
    gap: 8px;
  }
  .brand__mark {
    width: 12px;
    height: 12px;
    background: var(--fern);
  }
  .brand__name {
    font-family: "Dosis", sans-serif;
    font-weight: 500;
    font-size: 20px;
    color: var(--charcoal);
    letter-spacing: 0.2px;
  }
  .contact {
    position: absolute;
    left: 336px;
    top: 37px;
    padding-left: 9px;
    border-left: 1.5px solid var(--fern);
    font-family: "Arimo", sans-serif;
    font-size: 6.4px;
    line-height: 8px;
    color: var(--ink);
  }
  .contact p { margin: 0 0 8px; }
  .contact p:last-child { margin-bottom: 0; }
  .contact__label {
    font-weight: 700;
    color: var(--fern-dark);
  }
  .footer-wave {
    position: absolute;
    left: 0;
    bottom: 0;
    width: 477px;
    height: 40px;
    display: block;
  }
</style>
</head>
<body>
<main class="canvas">
  <section class="sheet sheet--front" aria-label="Letterhead front">
    <header class="brand">
      <span class="brand__mark"></span>
      <span class="brand__name">Ferncove Law Group</span>
    </header>
    <address class="contact">
      <p>418 Alder Row, Suite #1200<br>Marlow City, ST 00010</p>
      <p>92 Harbor Lane<br>Eastbrook, ST 00021</p>
      <p><span class="contact__label">Tel:</span> 555-013-8274<br><span class="contact__label">Web:</span> ferncoveadvice.example</p>
    </address>
    <svg class="footer-wave" viewBox="0 0 477 40" preserveAspectRatio="none" aria-hidden="true">
      <path d="M0 22 C120 8 280 -2 477 20 L477 40 L0 40 Z" fill="var(--charcoal)"/>
      <path d="M0 31 C130 18 290 6 477 25 L477 40 L0 40 Z" fill="var(--silver)"/>
      <path d="M0 40 C150 26 300 12 477 30 L477 40 Z" fill="var(--paper)"/>
      <path d="M0 40 L240 40 C300 22 380 18 477 34 L477 40 Z" fill="var(--fern)"/>
      <path d="M330 24 C400 18 450 26 477 34 L477 37 C440 30 390 24 330 24 Z" fill="var(--charcoal)"/>
    </svg>
  </section>
  <section class="sheet sheet--back" role="img" aria-label="Letterhead reverse side with a light green chevron pattern"></section>
</main>
</body>
</html>
```